Equine Horse Employment site

We need to redesign the layout of Stablemark Hire.co.uk

It will offer Job seekers and Employers the place to look for a job, and look for a candidate.

The logical format needs to be improved and the layout must look highly visually appealing.

It needs to be incredibly simple to use and one click access to any part of the site.

The homepage must convey the following

- Log in and register areas
- Current Job Listings
- Current CV's
- Exclusive Service Club button
- Search box to allow simple searching for Jobs or CVs

We need PSD layouts for Homepage, Job listing Page, CV listing Page, Job Profile and CV Profile. This job is for the design of 5 PSD screens.

Generic page for ancillary page such as about, contact and news.

The biggest competitor is PaddockPost.com

Please ask us any questions and please be prepared to make changes, as we are very particular.

More work will be provided to the winning designer.

thanks

• It must not look cheap or like a job board, it has to have character and feel friendly, and inviting. Please do not submit poor designs that look like a job board, as they will be rejected instantly.

thanks

```html
<!DOCTYPE html>
<html lang="en">
<head>
<meta charset="utf-8">
<title>Stablemark Hire – Equine Sales Consultant</title>
<link href="https://fonts.googleapis.com/css2?family=Arimo:wght@400;700&display=swap" rel="stylesheet">
<style>
:root{
  --dark:#3f3b3c;
  --dark-2:#2a2829;
  --red:#d9493a;
  --red-2:#c23a2c;
  --blue:#5b95c3;
  --blue-btn:#72aedb;
  --text:#333;
  --muted:#666;
  --line:#e2e2e2;
  --card-border:#d6d6d6;
  --teal:#2f9aa8;
  --white:#fff;
}
*{box-sizing:border-box;margin:0;padding:0}
html,body{width:1009px;height:1200px;overflow:hidden;background:var(--white)}
body{font-family:"Arimo",Arial,sans-serif;color:var(--text)}
.page{position:relative;width:986px;height:1173px;transform:scale(1.0233);transform-origin:0 0}
.abs{position:absolute}

/* top bar */
.topbar{left:0;top:0;width:986px;height:27px;background:var(--dark)}
.tab{top:4px;height:23px;border-radius:3px 3px 0 0;font-size:13px;font-weight:700;text-align:center;line-height:23px}
.tab--seekers{left:161px;width:91px;background:var(--white);color:#444}
.tab--employers{left:258px;width:86px;background:var(--red);color:var(--white)}
.post-prompt{left:602px;top:7px;font-size:13px;font-weight:700;color:var(--white)}
.btn-click{left:739px;top:3px;width:78px;height:21px;background:var(--red);border-radius:3px;color:var(--white);font-size:13px;font-weight:700;text-align:center;line-height:21px}

/* header */
.brand{left:166px;top:56px;display:flex;align-items:center;gap:10px}
.brand-mark{width:26px;height:26px;background:var(--red);border-radius:2px}
.brand-name{font-size:20px;color:#2b2b2b;letter-spacing:1px}
.field{top:80px;width:100px;height:17px;border:1px solid #c9c9c9;font-size:9px;color:#999;padding:3px 5px}
.field--user{left:483px}
.field--pass{left:592px}
.btn-small{top:79px;height:17px;border-radius:2px;color:var(--white);font-size:10px;font-weight:700;text-align:center;line-height:17px}
.btn-signin{left:699px;width:51px;background:var(--blue-btn)}
.btn-register{left:755px;width:60px;background:var(--red)}

/* nav */
.mainnav{left:165px;top:114px;width:651px;height:26px;background:linear-gradient(#4a4647,var(--dark-2));border-radius:2px;display:flex}
.mainnav a{color:var(--white);font-size:11px;text-decoration:none;padding:0 14px;line-height:26px;border-right:1px solid #555}

/* card */
.card{left:165px;top:149px;width:651px;height:822px;border:1px solid var(--card-border);border-radius:2px;box-shadow:0 1px 2px rgba(0,0,0,.08)}
.job-title{left:182px;top:165px;width:420px;font-size:19px;font-weight:700;line-height:24px;color:#333}
.pin{left:609px;top:168px}
.employer{left:636px;top:168px}
.employer-name{font-size:13px;font-weight:700;color:#222}
.employer-loc{font-size:10px;color:var(--muted);margin-top:2px}
.employer-date{font-size:12px;font-weight:700;color:var(--blue);margin-top:4px}
.divider{height:1px;background:var(--line)}
.div-top{left:166px;top:220px;width:649px}
.div-bottom{left:166px;top:916px;width:649px}

.section-head{font-size:13px;font-weight:700;color:var(--blue)}
.info{font-size:9px;color:#444;border-collapse:collapse}
.info td{border-bottom:1px solid #ececec;padding:3px 0 3px 4px;vertical-align:top;line-height:10.5px}
.info td:first-child{width:98px}
.info--job{left:184px;top:257px;width:291px}
.info--yard{left:499px;top:257px;width:267px}
.info--yard td:first-child{width:98px}

.desc{left:184px;width:580px}
.desc p{font-size:9px;color:#555;line-height:17px;margin:7px 0 0 3px}

/* actions */
.btn-action{top:930px;height:28px;border-radius:2px;color:var(--white);font-size:12px;font-weight:700;text-align:center;line-height:28px}
.btn-apply{left:185px;width:132px;background:var(--blue-btn)}
.btn-save{left:328px;width:105px;background:var(--red)}
.print{left:446px;top:936px;display:flex;align-items:center;gap:7px;font-size:13px;font-weight:700;color:#777}
.share{top:936px;width:18px;height:18px;background:#8a8a8a;border-radius:2px}

/* footer */
.footer{left:0;top:990px;width:986px;height:183px;background:var(--dark)}
.foot-about{left:164px;top:1000px;width:270px;color:var(--white)}
.foot-about h3{font-size:15px;font-weight:700;margin-bottom:6px}
.foot-about p{font-size:8.5px;line-height:10.5px}
.foot-social{left:164px;top:1101px;display:flex;gap:7px}
.foot-social span{width:17px;height:17px;background:#d8d8d8;border-radius:2px}
.foot-col{top:1002px;color:var(--white)}
.foot-col h4{font-size:12px;font-weight:700;margin-bottom:9px}
.foot-col li{list-style:none;font-size:9px;line-height:15.3px}
.foot-rule{left:0;top:1135px;width:986px;height:1px;background:#555}
.copyright{left:0;top:1148px;width:929px;text-align:center;font-size:9px;color:var(--white)}
.copyright a{color:#8fb7d8;text-decoration:none}
</style>
</head>
<body>
<div class="page">

  <div class="abs topbar"></div>
  <div class="abs tab tab--seekers">Job seekers</div>
  <div class="abs tab tab--employers">Employers</div>
  <div class="abs post-prompt">Looking to Post a job?</div>
  <div class="abs btn-click">Click here</div>

  <div class="abs brand"><span class="brand-mark"></span><span class="brand-name">Stablemark Hire</span></div>
  <div class="abs field field--user">User name</div>
  <div class="abs field field--pass">Password</div>
  <div class="abs btn-small btn-signin">Sign in</div>
  <div class="abs btn-small btn-register">Register</div>

  <nav class="abs mainnav">
    <a href="#">Home</a><a href="#">About US</a><a href="#">Employers</a><a href="#">Advertise</a><a href="#">News</a><a href="#">Resources</a><a href="#">Helpful links</a>
  </nav>

  <div class="abs card"></div>
  <h1 class="abs job-title">Job: Equine Sales Consultant For Fernvale Uk, Uk, All, United kingdom</h1>
  <svg class="abs pin" width="20" height="24" viewBox="0 0 20 24" aria-hidden="true">
    <path d="M10 1a8 8 0 0 0-8 8c0 6 8 14 8 14s8-8 8-14a8 8 0 0 0-8-8z" fill="var(--teal)"/>
    <circle cx="10" cy="9" r="3" fill="#7cc9d3"/>
  </svg>
  <div class="abs employer">
    <div class="employer-name">brookmeadstables</div>
    <div class="employer-loc">Chobham, Surrey, United Kingdom</div>
    <div class="employer-date">Date:8/28/2012</div>
  </div>
  <div class="abs divider div-top"></div>

  <h2 class="abs section-head" style="left:184px;top:234px">The Job</h2>
  <table class="abs info info--job">
    <tr><td>Job No.</td><td>155</td></tr>
    <tr><td>Status</td><td>A world beating product in the pet, vet<br><br>&amp; equine health market</td></tr>
    <tr><td>Title</td><td>Equine Sales Consultant For Fernvale UK</td></tr>
    <tr><td>Type</td><td>Sales, Other</td></tr>
    <tr><td>Work type</td><td>Full time</td></tr>
    <tr><td>Salary</td><td>ote £20,000 (Commission only)</td></tr>
    <tr><td>Min Education</td><td>&nbsp;</td></tr>
    <tr><td>Live in</td><td>No</td></tr>
    <tr><td>Bring own horse</td><td>No</td></tr>
    <tr><td>Training available</td><td>Yes</td></tr>
    <tr><td>Posted</td><td>30/05/2012</td></tr>
    <tr><td>Updated</td><td>30/05/2012</td></tr>
  </table>

  <h2 class="abs section-head" style="left:499px;top:234px">The Yard</h2>
  <table class="abs info info--yard">
    <tr><td>Yard No.</td><td>1324</td></tr>
    <tr><td>Name</td><td>Fernvale Saddlery Ltd UK</td></tr>
    <tr><td>Location</td><td>United Kingdom</td></tr>
    <tr><td>Type</td><td>Shop/Retail, Online business, Other</td></tr>
  </table>

  <section class="abs desc" style="top:496px">
    <h2 class="section-head">Job Description</h2>
    <p>We have a variety of locations around the UK where we are looking to place self employed sales consultants to represent our full range of products in all regions over the UK and beyond, both to the Equine industry and veterinary surgeries. We are searching for motivated sales people to work on a self employed basis representing our full range of products in Equine Health &amp; Horse care products. The successful candidate will be able to demonstrate exceptional natural sales ability, be highly motivated, and target driven.</p>
  </section>
  <section class="abs desc" style="top:597px">
    <h2 class="section-head">Requirements</h2>
    <p>an individual territory and customer base will be provided to all consultants who show a willingness to perform and a flexible attitude towards working hours &amp; time spent on the road.</p>
  </section>
  <section class="abs desc" style="top:662px">
    <h2 class="section-head">Required Skills</h2>
    <p>The candidate must be first and foremost a passionate communicator and have a good understanding of the OfficeDesk software suite.</p>
  </section>
  <section class="abs desc" style="top:711px">
    <h2 class="section-head">Required Expertise</h2>
    <p>Previous experience in sales is not essential but it is preferred.</p>
  </section>
  <section class="abs desc" style="top:762px">
    <h2 class="section-head">Required Expertise</h2>
    <p>Previous experience in sales is not essential but it is preferred.</p>
  </section>
  <section class="abs desc" style="top:814px">
    <h2 class="section-head">Benefits</h2>
    <p>The successful candidate will be self-employed and can expect to earn in excess of £20,000 OTE Candidates must be car owners and must be available for interview on one of two dates as follows: 31st October in Stoke or 1st November in Guildford (details to follow)</p>
  </section>
  <h2 class="abs section-head" style="left:186px;top:880px">The Facility</h2>

  <div class="abs divider div-bottom"></div>
  <div class="abs btn-action btn-apply">Apply for this job</div>
  <div class="abs btn-action btn-save">Save this job</div>
  <div class="abs print">
    <svg width="21" height="18" viewBox="0 0 21 18" aria-hidden="true">
      <rect x="5" y="0" width="11" height="5" fill="#888"/>
      <rect x="0" y="5" width="21" height="9" rx="2" fill="#888"/>
      <rect x="5" y="11" width="11" height="7" fill="#bbb"/>
    </svg>
    Print this job
  </div>
  <span class="abs share" style="left:578px"></span>
  <span class="abs share" style="left:603px"></span>

  <footer>
    <div class="abs footer"></div>
    <div class="abs foot-about">
      <h3>About Stablemark Hire</h3>
      <p>Lorem Ipsum is simply dummy text of the printing and typesetting industry. Lorem Ipsum has been the industry's standard dummy text ever since the 1500s, when an unknown printer took a galley of type and scrambled it to make a type specimen book. It has survived not only five centuries, but also the leap into electronic typesetting, remaining essentially unchanged.</p>
    </div>
    <div class="abs foot-social"><span></span><span></span><span></span><span></span></div>
    <div class="abs foot-col" style="left:484px">
      <h4>Employers</h4>
      <ul><li>What you get</li><li>How we work</li><li>Register</li><li>Login</li><li>Groom Search</li><li>FAQs</li></ul>
    </div>
    <div class="abs foot-col" style="left:576px">
      <h4>Grooms</h4>
      <ul><li>What you get</li><li>How we work</li><li>Register CV</li><li>Login</li><li>Job Search</li><li>FAQs</li></ul>
    </div>
    <div class="abs foot-col" style="left:660px">
      <h4>Featured jobs</h4>
      <ul><li>Head Groom</li><li>Stallion Hander - Australia</li><li>Instructor rider</li><li>Riding Instructor</li><li>Polo Groom</li><li>secretary/admin/telesales</li></ul>
    </div>
    <div class="abs foot-rule"></div>
    <div class="abs copyright">Copyright Stablemark Hire 2012. Use of this website constitutes acceptance of our <a href="#">User Agreement and Privacy Policy</a></div>
  </footer>

</div>
</body>
</html>
```